electronic happy holidays card

Need a quick designed holiday card that we can email out and post to our social medias. We are a mobile thermal printer company based in Michigan. We sell to resellers and endusers worldwide. The card needs to say happy holidays or season greetings.

Needs to say in the card: "Wishing you a happy holiday season with all the best wishes for the New Year.

Your friends at Corvane, LLC.

Target Market(s)

resellers, distributors, end-users world wide.

Industry/Entity Type

Electronic

```html
<!DOCTYPE html>
<html lang="en">
<head>
<meta charset="utf-8">
<title>Corvane Holiday Greeting</title>
<link rel="stylesheet" href="https://fonts.googleapis.com/css2?family=Great+Vibes&family=Oswald:wght@300;600&display=swap">
<style>
  :root {
    --snow-white: #fbfaf7;
    --silver-mist: #e6e3dc;
    --silver-deep: #d6d1c7;
    --gold-script: #a88a3e;
    --gold-brand: #8b7350;
    --gold-ornament: #c4ad70;
    --gold-shadow: #a98f52;
    --tagline-white: #ffffff;
    --pine-frost: #eef0ee;
  }
  html, body {
    margin: 0;
    padding: 0;
    width: 1200px;
    height: 1200px;
    overflow: hidden;
    background: var(--snow-white);
  }
  .card {
    position: relative;
    width: 1200px;
    height: 1200px;
    overflow: hidden;
    background:
      radial-gradient(ellipse 1000px 600px at 50% 20%, #ffffff 0%, rgba(255,255,255,0) 70%),
      linear-gradient(180deg, var(--silver-mist) 0%, #efede8 30%, var(--silver-deep) 46%, #f5f3ef 60%, #f3f1ec 78%, var(--silver-mist) 90%, #ebe8e2 100%);
  }
  .snow-drifts {
    position: absolute;
    inset: 0;
    width: 1200px;
    height: 1200px;
  }
  .branch-ornaments {
    position: absolute;
    left: 230px;
    top: 0;
    width: 680px;
    height: 680px;
    border-radius: 0 0 50% 50% / 0 0 46% 46%;
    background: linear-gradient(180deg, var(--pine-frost) 0%, #e6e8e5 40%, #ddd2b0 58%, var(--gold-ornament) 78%, var(--gold-shadow) 100%);
  }
  .greeting {
    position: absolute;
    left: 0;
    top: 770px;
    width: 1200px;
    margin: 0;
    text-align: center;
    font-family: "Great Vibes", cursive;
    font-weight: 400;
    font-size: 62px;
    line-height: 66px;
    color: var(--gold-script);
  }
  .values {
    position: absolute;
    left: 0;
    top: 930px;
    width: 1200px;
    display: flex;
    justify-content: center;
    align-items: center;
    gap: 16px;
    font-family: "Oswald", sans-serif;
    font-weight: 300;
    font-size: 22px;
    line-height: 30px;
    letter-spacing: 2px;
    color: var(--tagline-white);
  }
  .values .rule {
    width: 40px;
    height: 2px;
    background: var(--tagline-white);
  }
  .brand {
    position: absolute;
    left: 0;
    top: 1044px;
    width: 1200px;
    display: flex;
    justify-content: center;
    align-items: center;
    gap: 16px;
    font-family: "Oswald", sans-serif;
    font-weight: 600;
    font-size: 60px;
    line-height: 72px;
    letter-spacing: 3px;
    color: var(--gold-brand);
  }
  .brand .mark {
    width: 46px;
    height: 46px;
    background: var(--gold-brand);
  }
</style>
</head>
<body>
  <main class="card">
    <svg class="snow-drifts" viewBox="0 0 1200 1200" aria-hidden="true">
      <path d="M0 600 C 300 540, 700 660, 1200 580 L1200 760 C 800 720, 400 780, 0 740 Z" fill="#ffffff" opacity="0.35"/>
      <path d="M0 1000 C 350 950, 800 1040, 1200 980 L1200 1200 L0 1200 Z" fill="#ffffff" opacity="0.4"/>
    </svg>

    <div class="branch-ornaments" role="img" aria-label="Frosted white pine branch with three gold bauble ornaments hanging on strings"></div>

    <p class="greeting">Wishing you a happy holiday season<br>with all the best wishes for the New Year !</p>

    <div class="values">
      <span class="rule"></span>
      <span>LOVE • PEACE • HAPPINESS</span>
      <span class="rule"></span>
    </div>

    <div class="brand">
      <span class="mark"></span>
      <span class="brand-name">CORVANE</span>
    </div>
  </main>
</body>
</html>
```